executive development which breaks down traditional practices and thought processes

4 or 5 page website. Home page idea is fixed but needs creative execution to work {see attachment}, branding, as in corporate identity is in place and ready to go, (see attachment). Site needs to reflect the the market and typical participant, which are very high achievers up to and including Board Level Members in 'world leading company's'.

What we do is different, we are often copied, but without the success.

We require simple, slick impact, we have powerful messages that need to be supported by exquisite, simplistic design. We know we are the best out there and have kept our heads under water, but now is the time to start our expansion process.

We have copywriters briefed, and are liking what we read, so time to engage with designers who might like to 'wow' us, as well as our existing and potential clients.

Pages to include a standard landing/home page, about us, methodology, testimonials/awards and let's talk pages. Our philosophy is: opening minds to new ways of thinking, being, working and acting; to challenge long held business, management and leadership biases.

Our experiential learning technique is branded 'Kestrel' where we take people out of their comfort zone or into new & very different environments; to experience the way methodology and leadership techniques from uncomfortable encounters can be beneficial in big business strategic decision making, being more innovative and solving leadership & managerial challenges with new eyes (or a new perspective).

We will need to include video clips for awards we have won and testimonials from participants and company's alike. We work across the globe, the site needs to reflect this, without us looking like a huge corporate company, which we are not. We are small but pack a powerful punch, and that's the way we like it. Our clients don't see us as consultants or suppliers, more as the missing cog or the oil in the machine to get their executives to engage and deliver unorthodox thought processes which keep them at the forefront of their industries.

Both the copywriters and ourselves see typography being a crucial element to the impact of the site, so those designers with a passion in this area may well find our preference.

We are ready to go, good luck.

sorry guys missing the brief by a long way, we always said we were not looking for an off the shelf solution/concept which could be created on any 'tin kettle' like ortal and to be honest that's all we have received

Reason: designs miss the brief

Reason: We are not getting the desired simplistic landing page required.

```html
<!DOCTYPE html>
<html lang="en">
<head>
<meta charset="utf-8">
<title>Ardent Executive Development</title>
<link href="https://fonts.googleapis.com/css2?family=Lato:wght@300;400&display=swap" rel="stylesheet">
<style>
  :root {
    --backdrop: #ebebeb;
    --page: #ffffff;
    --ink: #111111;
    --black: #000000;
    --field: #ebebeb;
    --muted: #999999;
    --brand-green: #3daa47;
    --brand-purple: #663399;
    --rule-purple: #6a2f8f;
    --rule-dark: #444444;
    --grey-text: #888888;
  }
  * { margin: 0; padding: 0; box-sizing: border-box; }
  html, body { width: 1200px; height: 1000px; overflow: hidden; }
  body { background: var(--backdrop); font-family: "Lato", Arial, sans-serif; font-weight: 300; color: var(--ink); }
  h1, h2, h3 { font-weight: 300; }
  .page { position: absolute; left: 256px; top: 0; width: 678px; height: 1000px; background: var(--page); }
  .abs { position: absolute; }

  .brand { display: flex; align-items: center; gap: 6px; }
  .brand-name { font-size: 40px; font-weight: 400; color: var(--brand-green); line-height: 1; letter-spacing: -1px; }
  .brand-mark { width: 10px; height: 10px; background: var(--brand-purple); }
  .brand-tag { font-size: 7px; color: var(--grey-text); font-weight: 400; }

  .main-nav { left: 321px; top: 30px; display: flex; gap: 19px; font-size: 9.5px; font-weight: 400; }

  .hero-photo { left: 0; top: 71px; width: 238px; height: 162px; background: linear-gradient(135deg, #a9a9a9 0%, #c98a95 30%, #8f9a6a 55%, #d9a06a 75%, #cfcfcf 100%); }
  .hero-person { left: 28px; top: 233px; width: 148px; height: 93px; background: linear-gradient(#e0bfa8 0%, #c9a08a 35%, #1e1e22 75%); }
  .hero-statement { left: 238px; top: 71px; width: 440px; height: 162px; background: var(--black); color: #fff; font-size: 24px; line-height: 30px; padding: 16px 20px 0 34px; }

  .intro { left: 208px; top: 265px; width: 446px; font-size: 8.5px; line-height: 11.8px; font-weight: 400; letter-spacing: -0.1px; }

  .section-title { font-size: 20px; font-weight: 300; }
  .rule-dark { left: 26px; top: 390px; width: 628px; height: 1px; background: var(--ink); }
  .news-title { font-size: 21px; font-weight: 300; }
  .news-text { width: 330px; font-size: 8.6px; line-height: 12px; font-weight: 400; }
  .more-btn { width: 76px; height: 20px; background: var(--muted); color: #fff; font-size: 11px; text-align: center; line-height: 20px; font-weight: 400; }

  .video { left: 380px; top: 426px; width: 268px; height: 163px; border: 3px solid #8f8f8f; border-bottom: none; background: #fff; }
  .video-bar { position: absolute; left: -3px; right: -3px; bottom: 0; height: 13px; background: #1a1a1a; }
  .video-progress { position: absolute; left: 0; right: 0; top: 0; height: 2px; background: #b23; }
  .video-brand { position: absolute; left: 68px; top: 68px; }
  .video-play { position: absolute; left: 90px; top: 30px; }

  .rule-purple { left: 26px; top: 616px; width: 628px; height: 1px; background: var(--rule-purple); }

  .field { left: 24px; width: 335px; height: 33px; background: var(--field); font-size: 16px; line-height: 33px; padding-left: 9px; color: var(--ink); }
  .submit-btn { left: 22px; top: 830px; width: 108px; height: 36px; background: var(--black); color: #fff; font-size: 16px; text-align: center; line-height: 36px; }

  .quote-box { left: 379px; top: 676px; width: 270px; height: 196px; background: var(--brand-purple); color: #fff; font-size: 20px; line-height: 25px; padding: 27px 16px 0 18px; }

  .footer-rule { left: 0; top: 890px; width: 678px; height: 3px; background: var(--rule-dark); }
  .footer-phone { left: 79px; top: 962px; font-size: 12px; font-weight: 400; }
  .footer-nav { left: 188px; top: 909px; font-size: 9.5px; line-height: 14.3px; font-weight: 400; list-style: none; }
  .newsletter-label { left: 381px; top: 910px; font-size: 10.5px; font-weight: 400; }
  .newsletter-field { left: 380px; top: 929px; width: 277px; height: 23px; background: var(--field); font-size: 11px; line-height: 23px; padding-left: 10px; font-weight: 400; }
  .newsletter-btn { left: 379px; top: 962px; width: 50px; height: 17px; background: var(--black); color: #fff; font-size: 8px; text-align: center; line-height: 17px; font-weight: 400; }
</style>
</head>
<body>
<div class="page">
  <header>
    <div class="abs" style="left:28px; top:12px;">
      <div class="brand"><span class="brand-name">ardent</span><span class="brand-mark"></span></div>
      <div class="brand-tag" style="margin-left:57px;">Executive development</div>
    </div>
    <nav class="abs main-nav">
      <span>Home</span><span>About us</span><span>Methodology</span><span>Testimonials/awards</span><span>Let's talk</span>
    </nav>
  </header>

  <section>
    <div class="abs hero-photo" role="img" aria-label="Photo of a thoughtful businesswoman looking up at coloured question-mark speech bubbles"></div>
    <div class="abs hero-person" role="img" aria-label="Lower part of the businesswoman photo, dark jacket"></div>
    <div class="abs hero-statement">Opening minds to new ways of thinking, being, working and acting; to challenge long held business, management and leadership biases.</div>
    <p class="abs intro">Our experiential learning technique is branded 'Kestrel' where we take people out of their comfort zone or into new &amp; very different environments; to experience the way methodology and leadership techniques from uncomfortable encounters can be beneficial in big business strategic decision making, being more innovative and solving leadership &amp; managerial challenges with new eyes (or a new perspective).</p>
  </section>

  <section>
    <h2 class="abs section-title" style="left:26px; top:362px;">Latest news</h2>
    <div class="abs rule-dark"></div>

    <h3 class="abs news-title" style="left:27px; top:404px;">Kestrel</h3>
    <p class="abs news-text" style="left:27px; top:439px;">Our experiential learning technique is branded 'Kestrel' where we take people out of their comfort zone or into new &amp; very different environments</p>
    <div class="abs more-btn" style="left:286px; top:471px;">more...</div>

    <h3 class="abs news-title" style="left:27px; top:496px;">Kestrel</h3>
    <p class="abs news-text" style="left:27px; top:531px;">Our experiential learning technique is branded 'Kestrel' where we take people out of their comfort zone or into new &amp; very different environments</p>
    <div class="abs more-btn" style="left:286px; top:570px;">more...</div>

    <div class="abs video">
      <div class="video-brand"><span class="brand-name" style="font-size:34px;">ardent</span></div>
      <svg class="video-play" width="90" height="90" viewBox="0 0 90 90">
        <circle cx="45" cy="45" r="44" fill="#bdbdbd" fill-opacity="0.85" stroke="#e6e6e6" stroke-width="2"/>
        <polygon points="34,25 34,65 66,45" fill="#ffffff"/>
      </svg>
      <div class="video-bar"><div class="video-progress"></div></div>
    </div>

    <div class="abs rule-purple"></div>
  </section>

  <section>
    <h2 class="abs section-title" style="left:25px; top:637px;">Lets talk</h2>
    <div class="abs field" style="top:675px;">Name</div>
    <div class="abs field" style="top:723px;">Email</div>
    <div class="abs field" style="top:777px;">Message</div>
    <div class="abs submit-btn">Submit</div>

    <h2 class="abs section-title" style="left:381px; top:637px;">What our clinets are saying</h2>
    <blockquote class="abs quote-box">“Great service. I really leanrt alot from ardent and will be enjoying he benfits for a long time to come.”</blockquote>
  </section>

  <footer>
    <div class="abs footer-rule"></div>
    <div class="abs" style="left:19px; top:914px;">
      <div class="brand"><span class="brand-name" style="font-size:38px;">ardent</span><span class="brand-mark"></span></div>
      <div class="brand-tag" style="margin-left:56px;">Executive development</div>
    </div>
    <div class="abs footer-phone">01632 960418</div>
    <ul class="abs footer-nav">
      <li>Home</li><li>About us</li><li>Methodology</li><li>Testimonials/awards</li><li>Let's talk</li>
    </ul>
    <div class="abs newsletter-label">Sign up for our newsletter</div>
    <div class="abs newsletter-field">Email</div>
    <div class="abs newsletter-btn">Submit</div>
  </footer>
</div>
</body>
</html>
```